依頼詳細
【Tobiraのサービス特徴はこの3つ!】
●無料で請求書管理
請求書の作成・PDFダウンロードなどの機能はずっと無料でご利用になれます。顧客の数や、請求書の枚数に制限はありません。さらに有料プランなら見積り機能も使えます
●あんしんの印刷・郵送システム
Tobiraでは安全なドキュメントセンターで印刷、封入、封かん、発送を行なっています。それぞれの作業は機械が行うため請求書をの中身を人が見るということや人為的なミスはありません。詳しくはこちら
●どこでも請求書の作成・管理ができる
専用画面からログインすれば、書き方がわからなくてもテンプレートの必要事項を埋めるだけで出張先や自宅、iPad、スマートフォンなどからいつでも作成・編集できます。

---------------------------------------------------------------------------------

今回は、2種類のデザインを採用させていただきます。
1件10万円で、2種類の募集となりますので、
ドド~ンと総額20万円のキャンペーンとなります。
記載項目
■ 希望するデザイン
フリーランスのエンジニアさん、デザイナーさんが使いたくなる、オシャレで格好いい請求書の、オリジナルのデザインをご提案ください。

また、以下内容は請求書面として必要な事項となりますので必ず記載ください。
(現状の請求書のデータをアップロードしておりますので参照・活用ください)
・請求年月日
・請求先名称
・請求元(名前、住所、TEL、FAX、メールアドレス)
・請求元印影画像
・請求金額合計
・請求明細(20行、小計、消費税、合計金額)
・備考欄(3行)
・振込口座欄(1行)
希望イメージ
• +5 0 +5
• シンプル
複雑
• 単色
カラフル
• 暗い
明るい
• 日常
高級
• 遊び心
厳粛
• 未来的
伝統的
• 女性的
男性的
希望する色
色の指定はございません
納品ファイル
• イラストレーター形式 (.ai)
• フォトショップ形式 (.psd)
補足説明
■ 納品ファイルの希望
Illustrator形式、Photoshop形式、Fireworks形式
(最大容量は1024kbとしてそれ以下で作ってください)
依頼公開後の追記内容
■ 選んだ理由

bluewhistlerさんの作品は、どの業種でも使いやすく受け取り手も安心できるデザインということで選ばせて頂きました

もう一点は(http://www.kumoshi-hub.jp/work/proposal/5830417)になります。(現在システムの都合で当選にできていません)
k-atelierさんの作品は請求書のかっちりした感じに少し遊びを加えた感じのバランスがよく、採用しました。

■ 提案者全員のお礼・コメント

これほど多くの応募をいただけるとは思っておらずとても驚くとともに、感謝の気持でいっぱいです。

請求書のデザインということで、単純にデザイン性だけでは判断できず、どれも素敵な作品ばかりだったので選定には本当に時間がかかりました。

今回の当選作品以外にもTobira賞として10点ほど買取のオファーを出させて頂きます。どうぞよろしくおねがいします。

この度は本当にご応募ありがとうございました。

```html
<!DOCTYPE html>
<html lang="ja">
<head>
<meta charset="utf-8">
<title>請求書</title>
<link href="https://fonts.googleapis.com/css2?family=Noto+Sans+JP:wght@400;500;700&family=Roboto:ital,wght@1,900&display=swap" rel="stylesheet">
<style>
:root{
  --brown:#4b3a2c;
  --brown-dark:#3a2c21;
  --ink:#2b2b2b;
  --muted:#6a6a6a;
  --line:#5a4a3c;
  --row-alt:#efedea;
  --row:#ffffff;
  --paper:#ffffff;
  --band-top:#cfcfcf;
  --band-bot:#f4f4f4;
  --seal:#d94a5a;
  --invoice:#9a9a9a;
}
*{box-sizing:border-box;margin:0;padding:0}
html,body{width:846px;height:1200px;overflow:hidden;background:var(--paper)}
body{font-family:"Noto Sans JP",sans-serif;color:var(--ink);position:relative}
.header-band{position:absolute;left:0;top:0;width:846px;height:150px;background:linear-gradient(180deg,#bdbdbd 0%,#e6e6e6 60%,#fff 100%)}
.footer-band{position:absolute;left:0;bottom:0;width:846px;height:150px;background:linear-gradient(0deg,#c4c4c4 0%,#e8e8e8 55%,#fff 100%)}
.title{position:absolute;left:34px;top:16px;display:flex;gap:4px}
.title span{width:66px;height:66px;background:var(--brown);color:#fff;font-size:40px;font-weight:500;display:flex;align-items:center;justify-content:center}
.meta{position:absolute;left:260px;top:18px;font-size:12px}
.meta-row{display:flex;height:26px;margin-bottom:6px;align-items:center}
.meta-label{width:70px;height:100%;background:var(--brown);color:#fff;display:flex;align-items:center;padding-left:8px;letter-spacing:2px}
.meta-value{width:230px;height:100%;background:rgba(255,255,255,.75);display:flex;align-items:center;padding-left:10px;font-size:13px}
.client{position:absolute;left:50px;top:188px;width:420px;border-bottom:2px solid var(--line);padding-bottom:4px;display:flex;justify-content:space-between;align-items:flex-end}
.client-name{font-size:30px;font-weight:500;letter-spacing:1px}
.client-honor{font-size:22px;margin-right:40px}
.lead{position:absolute;left:50px;top:276px;font-size:14px}
.total-due{position:absolute;left:50px;top:308px;width:340px;border-bottom:2px solid var(--line);display:flex;align-items:flex-end;padding-bottom:4px}
.total-due .label{font-size:18px;width:130px}
.total-due .amount{font-size:32px;font-weight:500}
.issuer{position:absolute;left:500px;top:186px;width:310px}
.issuer-name{font-size:21px;font-weight:500;border-bottom:1px solid var(--line);padding-bottom:6px;width:290px}
.issuer-addr{font-size:11px;line-height:16px;margin-top:16px;color:var(--ink)}
.issuer-contact{font-size:11px;line-height:16px;margin-top:24px}
.seal{position:absolute;left:708px;top:226px;width:98px;height:92px;background:var(--seal)}
.items{position:absolute;left:50px;top:403px;width:754px}
.items .row{display:grid;grid-template-columns:1fr 72px 88px 82px;height:23.3px;align-items:center;font-size:12px;background:var(--row)}
.items .row:nth-child(even){background:var(--row-alt)}
.items .head{background:var(--brown)!important;color:#fff;height:26px;font-size:12px;letter-spacing:2px}
.items .head div{text-align:center}
.items .row div{padding:0 8px}
.items .num{text-align:right}
.items .qty{text-align:center}
.remarks{position:absolute;left:50px;top:908px;width:460px;border:1px solid var(--line);font-size:12px}
.remarks div{height:23px;line-height:23px;padding-left:10px;border-bottom:1px solid #999}
.remarks div:last-child{border-bottom:none}
.summary{position:absolute;left:520px;top:908px;width:284px;font-size:12px}
.summary .line{display:flex;justify-content:space-between;height:30px;align-items:center;padding:0 8px;border-bottom:1px solid #999}
.summary .line:first-child{border-top:1px solid var(--line)}
.summary .grand{border-bottom:2px solid var(--line)}
.bank{position:absolute;left:22px;top:1018px;display:flex;align-items:center;width:782px}
.bank-label{width:120px;height:64px;background:var(--brown);color:#fff;font-size:14px;display:flex;align-items:center;justify-content:center;letter-spacing:2px}
.bank-body{margin-left:22px;font-size:13px;line-height:22px;border-bottom:1px solid var(--line);padding-bottom:4px;width:540px}
.bank-note{font-size:11px;color:var(--muted)}
.invoice-mark{position:absolute;right:36px;top:1112px;font-family:"Roboto",sans-serif;font-style:italic;font-weight:900;font-size:54px;color:var(--invoice);letter-spacing:1px}
</style>
</head>
<body>
<div class="header-band"></div>
<div class="footer-band"></div>

<h1 class="title" aria-label="請求書"><span>請</span><span>求</span><span>書</span></h1>

<div class="meta">
  <div class="meta-row"><div class="meta-label">発 行 日</div><div class="meta-value">2013年05月11日</div></div>
  <div class="meta-row"><div class="meta-label">請求番号</div><div class="meta-value">20130511-005</div></div>
</div>

<div class="client"><span class="client-name">サンプル株式会社</span><span class="client-honor">様</span></div>
<p class="lead">下記のとおりご請求申し上げます。</p>
<div class="total-due"><span class="label">ご請求金額</span><span class="amount">￥84,000 -</span></div>

<div class="issuer">
  <div class="issuer-name">ミドリノ工房株式会社</div>
  <div class="issuer-addr">〒460-0000<br>愛知県名古屋市中区<br>栄町1丁目2番3号<br>サンプルビル5F</div>
  <div class="issuer-contact">TEL:052-000-1234<br>FAX:052-000-1235<br>office@midorino-kobo.jp</div>
</div>
<div class="seal" role="img" aria-label="請求元の角印"></div>

<div class="items">
  <div class="row head"><div>品番・品名</div><div>数 量</div><div>単 価</div><div>金 額</div></div>
  <div class="row"><div>デザイン</div><div class="qty">1</div><div class="num">20,000</div><div class="num">20,000</div></div>
  <div class="row"><div>企画・取材費用</div><div class="qty">1</div><div class="num">60,000</div><div class="num">60,000</div></div>
  <div class="row"><div></div><div></div><div></div><div></div></div>
  <div class="row"><div></div><div></div><div></div><div></div></div>
  <div class="row"><div></div><div></div><div></div><div></div></div>
  <div class="row"><div></div><div></div><div></div><div></div></div>
  <div class="row"><div></div><div></div><div></div><div></div></div>
  <div class="row"><div></div><div></div><div></div><div></div></div>
  <div class="row"><div></div><div></div><div></div><div></div></div>
  <div class="row"><div></div><div></div><div></div><div></div></div>
  <div class="row"><div></div><div></div><div></div><div></div></div>
  <div class="row"><div></div><div></div><div></div><div></div></div>
  <div class="row"><div></div><div></div><div></div><div></div></div>
  <div class="row"><div></div><div></div><div></div><div></div></div>
  <div class="row"><div></div><div></div><div></div><div></div></div>
  <div class="row"><div></div><div></div><div></div><div></div></div>
  <div class="row"><div></div><div></div><div></div><div></div></div>
  <div class="row"><div></div><div></div><div></div><div></div></div>
  <div class="row"><div></div><div></div><div></div><div></div></div>
  <div class="row"><div></div><div></div><div></div><div></div></div>
</div>

<div class="remarks">
  <div>サンプル（備考欄1行目）</div>
  <div>サンプル（備考欄2行目）</div>
  <div></div>
</div>

<div class="summary">
  <div class="line"><span>小 計</span><span>80,000</span></div>
  <div class="line"><span>消費税(5%)</span><span>4,000</span></div>
  <div class="line grand"><span>合計金額</span><span>84,000</span></div>
</div>

<div class="bank">
  <div class="bank-label">お振込先</div>
  <div class="bank-body">日本サンプル銀行 中央支店 普通口座 01234567 サンプル（カ<br><span class="bank-note">※お振込み手数料はご負担願います。</span></div>
</div>

<div class="invoice-mark">INVOICE</div>
</body>
</html>
```